Velmora Outcomes Brochure Design Project

- Who we are?
Velmora Outcomes is New Internet Marketing Company Based in China.

It is our aim to provide Chinese clients with the means to internationally market their product, via the Internet.

Our primary products are Outsourced Design ( Thanks to Pixel hive and the amazing designers who use it), SEO and Virtual Hosting.

- Project Brief
Design a vibrant and fresh brochure that introduces the fundamentals of SEO. There is no restriction to the number of pages, however all the info I have included in this brief must be included.

- Colour Palette
Please see link or download the Adobe Swatch Exchange File or follow the link below
http://tintaro.example.com/#themes/search?term=5830716
Updates

Logo updated - grey background removed

Various file formats added for logo and brochure content

Brochure zip file add containing logo in different formats.

Adobe color scheme file added

The general corporate colors are:

Base Color: CMYK :0, 60, 80, 0  Hex: FF6633
Dark Orange: CMYK: 0, 72, 96, 30 Hex: B23308
Light Orange: CMYK 0, 42, 56, 0 Hex: FF9571
Grey: CMYK 0, 0, 0, 48 Hex: 858585
Light Grey: CMYK 0, 0, 0, 26 Hex: BDBDBD

Please note that I'm happy for other colors to be included, however I would like these the corporate branding colors to be clearly present through the brochure.

Hi All

First place payment has increased to $600 - Looking to see some creative designs!

Hi All

Project Deadline Extended
Reason: I have increase the budget and extend the deadline as I need to see more design.

I have attached a zip file that contains example brochures I like.

We are not keen on the table data its a little plain. We have create an info-graphic to replace one of the table and would like to see it included in the design.

Project Deadline Extended
Reason: A few designers have asked for this extension and I would like to see additional designs. Thanks Marek

Target Market(s)

- Our Target Audience is..
It is small to medium businesses looking to reach out to the international market.
Our clients still very much operate on a face to face level in business and are new to the concept of Internet marketing

However this must look professional, Marketable and Clean, with the power of connecting people globally, through SEO and design to be reflected visually in the brochure.

Industry/Entity Type

Internet

Requirements
Must have
• One or more of the FACTS that I have highlighted need to stand out on each page. These FACTS can be found the document attached to this brief and are under the section titled 'Did You Know!'. Not every fact in this section needs to be highlighted in the brochure, but each page needs to have at least, one or more fact that stands out, soemwhere on the page.
See attached document, under the heading 'Did you Know!' and use one or two of these facts to spruce up the pages!

One image/ per page or per two pages MUST be included!

- Provide stock photos and please send us a message with the additional cost of these with your submission

The Table data, that I have included in the attachment must be included in the body of the pages - BUT the table format is not necessary and you can place the information in the body like plain text.

The brochure size should be a little larger than A4.

Please design the back page, like a pocket to hold paper and other material in it that I include with this brochure.

```html
<!DOCTYPE html>
<html lang="en">
<head>
<meta charset="utf-8">
<title>Velmora Outcomes – Brochure Cover</title>
<link rel="stylesheet" href="https://fonts.googleapis.com/css2?family=Varela+Round&display=swap">
<style>
  :root {
    --base-orange: #ff6633;
    --cover-orange: #e8743a;
    --dark-orange: #b23308;
    --grey: #858585;
    --light-grey: #bdbdbd;
    --paper: #ffffff;
    --backdrop: #ececec;
    --photo-dark: #2a2a2a;
    --photo-mid: #8a8a8a;
    --photo-light: #d6d6d6;
  }
  html, body {
    margin: 0;
    width: 1200px;
    height: 1000px;
    overflow: hidden;
    background: var(--backdrop);
    font-family: "Varela Round", sans-serif;
  }
  .brochure-cover {
    position: absolute;
    left: 280px;
    top: 50px;
    width: 640px;
    height: 900px;
    background: var(--paper);
    box-shadow: 0 10px 30px rgba(0,0,0,0.12);
    overflow: hidden;
  }
  .cover-art {
    position: absolute;
    left: 0;
    top: 0;
    width: 640px;
    height: 520px;
  }
  .brand-lockup {
    position: absolute;
    right: 48px;
    top: 585px;
    display: flex;
    align-items: center;
    gap: 14px;
  }
  .brand-mark {
    width: 44px;
    height: 44px;
    border: 5px solid var(--cover-orange);
    border-radius: 50%;
    box-sizing: border-box;
  }
  .brand-name {
    font-size: 34px;
    color: var(--grey);
    letter-spacing: 0.2px;
  }
  .cover-footer {
    position: absolute;
    left: 48px;
    bottom: 70px;
  }
  .tagline {
    margin: 0 0 18px;
    font-size: 17px;
    line-height: 1.25;
    color: var(--grey);
  }
  .web-address {
    margin: 0;
    font-size: 17px;
    color: var(--cover-orange);
  }
</style>
</head>
<body>
  <main class="brochure-cover">
    <svg class="cover-art" viewBox="0 0 640 520" aria-hidden="false">
      <defs>
        <linearGradient id="cityTone" x1="0" y1="0" x2="1" y2="1">
          <stop offset="0" stop-color="var(--photo-dark)"/>
          <stop offset="0.5" stop-color="var(--photo-mid)"/>
          <stop offset="1" stop-color="var(--photo-light)"/>
        </linearGradient>
      </defs>
      <polygon class="accent-block" points="330,0 640,0 640,150 330,150" fill="var(--cover-orange)"/>
      <polygon class="night-street-photo" role="img" aria-label="Black and white photo of a city street at night with light trails"
               points="0,0 400,0 470,520 0,520" fill="url(#cityTone)"/>
      <polygon class="accent-overlay" points="290,0 400,0 470,520 330,520" fill="var(--cover-orange)" opacity="0.75"/>
    </svg>

    <div class="brand-lockup">
      <span class="brand-mark"></span>
      <span class="brand-name">Velmora Outcomes</span>
    </div>

    <div class="cover-footer">
      <p class="tagline">SEO, Logo Design &amp; Webdesign<br>for modern businesses</p>
      <p class="web-address">www.velmoraoutcomes.com</p>
    </div>
  </main>
</body>
</html>
```